Vantrell Law Letterhead

We need a new letterhead design for a Law Firm. The address for the law firm is 4817 Larkspur Boulevard, Suite 250, Houston, Texas 77342. Phone Number: 832-619-3057; Fax Number: 832-407-1694. The logo is uploaded to the project.

```html
<!DOCTYPE html>
<html lang="en">
<head>
<meta charset="utf-8">
<title>Vantrell Law Letterhead</title>
<link rel="stylesheet" href="https://fonts.googleapis.com/css2?family=Arimo:wght@400;700&family=Libre+Baskerville:wght@400;700&display=swap">
<style>
  :root {
    --bg: #d9d4cd;
    --paper: #ffffff;
    --ink: #1a1a1a;
    --navy: #1f2a5c;
    --crimson: #8e1a1e;
    --watermark: #eef0f5;
    --signature: #c9c9cf;
  }
  * { margin: 0; padding: 0; box-sizing: border-box; }
  html, body { width: 1200px; height: 900px; overflow: hidden; background: var(--bg); }
  .canvas { position: relative; width: 1200px; height: 900px; }
  .letterhead {
    position: absolute; left: 267px; top: 20px; width: 665px; height: 860px;
    background: var(--paper);
    box-shadow: 0 2px 10px rgba(0,0,0,0.18);
    font-family: "Arimo", Arial, sans-serif; color: var(--ink);
  }
  .brand {
    position: absolute; top: 40px; left: 0; right: 0;
    display: flex; justify-content: center; align-items: center; gap: 12px;
  }
  .brand-mark { width: 40px; height: 40px; border-radius: 50%; background: var(--navy); }
  .brand-name {
    font-family: "Libre Baskerville", Georgia, serif; font-weight: 400;
    font-size: 26px; color: var(--navy); letter-spacing: 0.5px;
  }
  .watermark {
    position: absolute; left: 246px; top: 428px; width: 170px; height: 170px;
    border-radius: 50%; background: var(--watermark);
  }
  .letter {
    position: absolute; left: 69px; right: 67px; top: 154px;
    font-size: 13.3px; line-height: 20.5px;
  }
  .date { margin-bottom: 32px; }
  .recipient-name { font-weight: 700; font-size: 14.5px; }
  .recipient { margin-bottom: 40px; }
  .body p { text-align: justify; }
  .body p + p { margin-top: 20.5px; }
  .signature {
    width: 84px; height: 22px; margin-top: 38px; border-radius: 3px;
    background: linear-gradient(90deg, var(--signature), #e4e4e8);
  }
  .sender { margin-top: 6px; font-size: 15.5px; }
  .footer {
    position: absolute; left: 0; right: 0; top: 801px;
    font-family: "Libre Baskerville", Georgia, serif; color: var(--navy);
    font-size: 9.5px; letter-spacing: 0.8px;
  }
  .footer-address { text-align: center; }
  .footer-row {
    display: flex; align-items: center; margin: 5px 23px 0; gap: 10px;
  }
  .footer-rule { flex: 1; height: 1.5px; background: var(--crimson); }
  .contact { display: flex; align-items: center; gap: 4px; }
  .contact svg { width: 10px; height: 10px; fill: var(--crimson); }
  .contacts { display: flex; gap: 14px; }
</style>
</head>
<body>
<div class="canvas">
  <section class="letterhead">
    <header class="brand">
      <span class="brand-mark"></span>
      <span class="brand-name">Vantrell Law</span>
    </header>

    <div class="watermark"></div>

    <main class="letter">
      <p class="date">4th September 20XX</p>
      <div class="recipient">
        <p class="recipient-name">Ronny Reader</p>
        <p>CEO, Company Name</p>
        <p>123 Address St</p>
        <p>Anytown, ST 12345</p>
      </div>
      <p>Dear Mr. Reader,</p>
      <div class="body">
        <p>Lorem ipsum dolor sit amet, consectetuer adipiscing elit, sed diam nonummy nibh euismod tincidunt ut laoreet dolore magna aliquam erat volutpat. Ut wisi enim ad minim veniam, quis nostrud exerci tation ullamcorper suscipit lobortis nisl ut aliquip ex ea commodo consequat.</p>
        <p>Duis autem vel eum iriure dolor in hendrerit in vulputate velit esse molestie consequat, vel illum dolore eu feugiat nulla facilisis at vero eros et accumsan.</p>
        <p>Nam liber tempor cum soluta nobis eleifend option congue nihil imperdiet doming id quod mazim placerat facer possim assum. Typi non habent claritatem insitam; est usus legentis in iis qui facit eorum claritatem. Investigationes demonstraverunt lectores legere me lius quod ii legunt saepius.</p>
      </div>
      <p>Sincerely,</p>
      <div class="signature" role="img" aria-label="Handwritten signature"></div>
      <p class="sender">Your Name</p>
    </main>

    <footer class="footer">
      <p class="footer-address">4817 Larkspur Boulevard, Suite 250, Houston, Texas 77342</p>
      <div class="footer-row">
        <span class="footer-rule"></span>
        <div class="contacts">
          <span class="contact">
            <svg viewBox="0 0 24 24" aria-hidden="true"><path d="M6.6 10.8a15.2 15.2 0 0 0 6.6 6.6l2.2-2.2a1 1 0 0 1 1-.25 11.4 11.4 0 0 0 3.6.57 1 1 0 0 1 1 1V20a1 1 0 0 1-1 1A17 17 0 0 1 3 4a1 1 0 0 1 1-1h3.5a1 1 0 0 1 1 1c0 1.25.2 2.45.57 3.6a1 1 0 0 1-.25 1z"/></svg>
            832-619-3057
          </span>
          <span class="contact">
            <svg viewBox="0 0 24 24" aria-hidden="true"><path d="M7 3h8v5H7zM3 9h18v11H3zm3 3v2h4v-2zm0 4v2h4v-2zm8-4v6h4v-6z"/></svg>
            832-407-1694
          </span>
        </div>
        <span class="footer-rule"></span>
      </div>
    </footer>
  </section>
</div>
</body>
</html>
```